Plakate für Haushaltsnahe Dienstleistungen sowie Alltagsbegleitung
Zielgruppe
Wir sind eine Firma die Haushaltsnahe Dienstleistungen sowie Alltagsbegleitung anbietet. Unser Hauptkundenklientel sind Pflegebedürftige Menschen denen Haushaltshilfe von der Pflegekasse zu steht.
Aufgabenstellung
Es soll ein Roll-Up werden. Es soll drauf stehen: Abrechnung mit allen Pflegekasse möglich über den Entlastungsbetrag (ab Pflegegrad 1 bis 5) sowie Verhinderungspflege. Kontaktdaten sowie unsere Vorteile sollen auch drauf stehen.

```html
<!DOCTYPE html>
<html lang="de">
<head>
<meta charset="utf-8">
<title>LINDHOF – Roll-Up Haushaltshilfe</title>
<link rel="stylesheet" href="https://fonts.googleapis.com/css2?family=Cinzel:wght@700&family=Fira+Sans:ital,wght@1,300&display=swap">
<style>
  :root {
    --brand-red: #c83a48;
    --deep-red: #b91c2c;
    --ink: #333333;
    --paper: #ffffff;
  }
  * { margin: 0; padding: 0; box-sizing: border-box; }
  html, body { width: 1200px; height: 2823px; overflow: hidden; background: var(--paper); }
  .rollup { position: relative; width: 1200px; height: 2823px; overflow: hidden; background: var(--paper); }
  .band { position: absolute; inset: 0; }
  .decor-area {
    position: absolute; left: 80px; top: 1760px; width: 1120px; height: 1063px;
    background: radial-gradient(ellipse at 60% 50%, rgba(185,28,44,0.55), rgba(185,28,44,0) 70%);
  }
  .brand {
    position: absolute; right: 60px; top: 130px;
    display: flex; align-items: center; gap: 22px;
  }
  .brand-dot { width: 44px; height: 44px; border-radius: 50%; background: var(--brand-red); }
  .brand-name {
    font-family: 'Fira Sans', sans-serif; font-style: italic; font-weight: 300;
    font-size: 72px; line-height: 1; color: var(--ink);
  }
  .headline {
    position: absolute; left: 50px; top: 548px; font-family: 'Cinzel', serif; font-weight: 700;
    font-size: 162px; line-height: 156px; color: var(--paper); letter-spacing: 1px;
  }
  .subline, .benefit, .contact { font-family: 'Fira Sans', sans-serif; font-style: italic; font-weight: 300; color: var(--paper); }
  .subline { position: absolute; left: 48px; top: 1045px; font-size: 64px; line-height: 88px; }
  .benefits { position: absolute; left: 20px; top: 1440px; list-style: none; }
  .benefit { position: relative; padding-left: 100px; font-size: 58px; line-height: 84px; }
  .benefit + .benefit { margin-top: 26px; }
  .benefit.is-third { margin-top: 64px; }
  .benefit.is-fourth { margin-top: 42px; }
  .benefit svg { position: absolute; left: 0; top: 50%; transform: translateY(-50%); width: 64px; height: 72px; }
  .contact { position: absolute; right: 66px; top: 2388px; text-align: right; font-size: 57px; line-height: 90px; font-style: italic; }
  .ornament { position: absolute; inset: 0; pointer-events: none; }
  .amp { font-family: 'Cinzel', serif; font-weight: 700; fill: var(--paper); }
</style>
</head>
<body>
<main class="rollup">
  <svg class="band" width="1200" height="2823" viewBox="0 0 1200 2823" aria-hidden="true">
    <polygon points="0,228 1200,440 1200,2823 0,2823" fill="var(--brand-red)"/>
  </svg>
  <div class="decor-area" role="img" aria-label="Große, dezente Markendekoration im Hintergrund"></div>

  <header class="brand">
    <span class="brand-dot" aria-hidden="true"></span>
    <span class="brand-name">LINDHOF</span>
  </header>

  <h1 class="headline">Ihre Haus-<br>haltshilfe<br>mit Herz!</h1>

  <p class="subline">Haushaltsnahe Dienstleisungen<br>und Alltagsbegeltiung für mehr<br>Lebensqualität!</p>

  <ul class="benefits">
    <li class="benefit"><svg viewBox="0 0 64 72"><path d="M6 42 L22 66 Q36 24 60 6" fill="none" stroke="#fff" stroke-width="6" stroke-linecap="round"/></svg>Abrechnung mit allen<br>Pflegekassen möglich</li>
    <li class="benefit"><svg viewBox="0 0 64 72"><path d="M6 42 L22 66 Q36 24 60 6" fill="none" stroke="#fff" stroke-width="6" stroke-linecap="round"/></svg>Abrechnung über den Entlastungs-<br>betrag von mind. 125 € mtl. ab Pfle-<br>gegrad 1 möglich</li>
    <li class="benefit is-third"><svg viewBox="0 0 64 72"><path d="M6 42 L22 66 Q36 24 60 6" fill="none" stroke="#fff" stroke-width="6" stroke-linecap="round"/></svg>Auch über die Verhinderungspflege</li>
    <li class="benefit is-fourth"><svg viewBox="0 0 64 72"><path d="M6 42 L22 66 Q36 24 60 6" fill="none" stroke="#fff" stroke-width="6" stroke-linecap="round"/></svg>Hilfe bei der Antragsstellung</li>
  </ul>

  <address class="contact">
    Lindenweg 14, 70173 Musterstadt<br>
    info@lindhof-hilfe.de<br>
    www.lindhof-haushalt.de<br>
    0123 45678900
  </address>

  <svg class="ornament" width="1200" height="2823" viewBox="0 0 1200 2823" aria-hidden="true">
    <g fill="none" stroke="#fff" stroke-width="18" stroke-linecap="round">
      <path d="M805 1250 Q880 1252 945 1295"/>
      <path d="M990 1452 Q960 1530 875 1610"/>
      <path d="M248 2192 Q185 2220 140 2285"/>
      <path d="M148 2460 Q270 2580 445 2608"/>
    </g>
    <g fill="#fff">
      <polygon points="862,1588 892,1626 860,1624"/>
      <polygon points="440,2586 470,2612 440,2636"/>
    </g>
    <text class="amp" x="948" y="1420" font-size="155">&amp;</text>
    <text class="amp" x="42" y="2420" font-size="155">&amp;</text>
  </svg>
</main>
</body>
</html>
```